V.Crest Gin - Bottle label Design

We are manufacturers of Gin in South Africa.
The name of our Gin is V.Crest Gin with Q standing for Vukhamba, a Xhosa Village in the region of Eastern Cape.

We would like our brand to depict the following (really the focus of Gold on it)
> Prosperity of the place
> Wealth of the place, land, material or in the people
> Gold rush, potential, hope

As the brand matures, we would like to have campaigns with it. See ideas below:
> V.Crest Premium
> Red dusk edition
Limited edition will be released every year
- V.Crest entabeni (location)
- V.Crest elwandle (location)

> Each batch of bottles with focus on a specific area/location in Vukhamba. One that is known and will be highlighted on the map design of the bottle.
Bottles based on landmarks in Vukhamba and landmark design in the Big V.

Below we tried but we are not where we really want to be in terms of Gin Bottle elegance.

Target Market(s)

Target market is the young crowd. Young Xhosa men and women working really hard to get their goals. Positive thinkers. Elegant. Fresh. Bold. Age from 24 to 45. People who enjoy quality products.

Industry/Entity Type

Beverage Industry. Craft Gin.

Font styles to use
Sans Serif
Decorative

Colors
FFF300
FFF600
FEFA6F
FFFEC7
FFFEE8
FFC000
F8CF3A
FAE287
FDF2CF
FEFAEE

Requirements
Must have
• Gold colour as a theme. Try and make the background textured.

```html
<!DOCTYPE html>
<html lang="en">
<head>
<meta charset="utf-8">
<title>V.Crest Gin – Bottle Label</title>
<link href="https://fonts.googleapis.com/css2?family=Josefin+Sans:wght@200&family=Roboto+Condensed:wght@400&display=swap" rel="stylesheet">
<style>
  :root {
    --page: #f2f0ea;
    --label: #fdfdfb;
    --ink: #1b1b1b;
    --rule: #6d6d6d;
    --gold-deep: #a8792a;
    --gold: #f8cf3a;
    --gold-light: #fae287;
    --gold-pale: #fdf2cf;
    --gold-cream: #fefaee;
    --earth: #8f6334;
    --map-tint: #f6f5f1;
  }
  * { box-sizing: border-box; margin: 0; padding: 0; }
  html, body { width: 1200px; height: 1200px; overflow: hidden; }
  body { background: var(--page); position: relative; }

  .label {
    position: absolute; left: 120px; top: 112px;
    width: 960px; height: 975px;
    background: var(--label);
  }

  .band {
    position: absolute; left: 20px; width: 936px; height: 47px;
    border-top: 2px solid var(--gold-deep);
    border-bottom: 2px solid var(--gold-deep);
    background:
      linear-gradient(90deg, var(--gold-pale), var(--gold-light) 20%, var(--gold-pale) 40%, var(--gold-light) 60%, var(--gold-pale) 80%, var(--gold-light));
  }
  .band::before {
    content: ""; position: absolute; left: 0; right: 0; top: 50%;
    border-top: 1px solid var(--gold);
  }
  .band--top { top: 5px; }
  .band--bottom { top: 889px; }

  .village-scene {
    position: absolute; left: 20px; top: 109px; width: 939px; height: 421px;
    background: linear-gradient(180deg,
      var(--gold-cream) 0%, var(--gold-pale) 14%,
      var(--earth) 28%, #b58a4c 40%,
      var(--gold-light) 55%, #e9dfc0 72%, #ece8dc 100%);
  }

  .route-map {
    position: absolute; left: 36px; top: 593px; width: 210px; height: 296px;
    background: var(--map-tint);
  }

  .brand-mark {
    position: absolute; left: 128px; top: 371px;
    width: 208px; height: 208px; border-radius: 50%;
    background: radial-gradient(circle at 35% 30%, var(--gold-light), var(--gold) 45%, var(--gold-deep));
  }
  .brand-name {
    position: absolute; left: 352px; top: 440px;
    font-family: "Josefin Sans", sans-serif; font-weight: 200;
    font-size: 160px; line-height: 1; color: var(--ink);
    letter-spacing: 2px; white-space: nowrap;
  }

  .facts {
    position: absolute; left: 20px; top: 690px; width: 936px; height: 195px;
    border: 2px dotted var(--rule);
    display: grid; grid-template-columns: 285px 370px 1fr; grid-template-rows: 103px 1fr;
  }
  .facts__type {
    grid-row: 1 / 3; border-right: 2px dotted var(--rule);
    font-family: "Josefin Sans", sans-serif; font-weight: 200;
    font-size: 136px; line-height: 1; color: var(--ink);
    display: flex; align-items: center; padding-left: 16px; padding-top: 30px;
  }
  .facts__cell {
    font-family: "Roboto Condensed", sans-serif; color: var(--ink);
    display: flex; align-items: center; justify-content: center;
    font-size: 32px;
  }
  .facts__tagline {
    grid-column: 2 / 4; border-bottom: 2px dotted var(--rule);
    letter-spacing: .6px;
  }
  .facts__abv { border-right: 2px dotted var(--rule); }
</style>
</head>
<body>
  <main class="label">
    <div class="band band--top" role="img" aria-label="Gold diamond pattern border"></div>

    <div class="village-scene" role="img" aria-label="Gold-toned sketch of Vukhamba village on a hillside with fences and houses"></div>

    <div class="route-map" role="img" aria-label="Faint street map of Vukhamba"></div>

    <div class="brand-mark"></div>
    <span class="brand-name">V.Crest</span>

    <section class="facts">
      <div class="facts__type">GIN</div>
      <div class="facts__cell facts__tagline">Our Golden Gift from Vukhamba to the World</div>
      <div class="facts__cell facts__abv">43% alc.vol.</div>
      <div class="facts__cell facts__volume">750 ml</div>
    </section>

    <div class="band band--bottom" role="img" aria-label="Gold diamond pattern border"></div>
  </main>
</body>
</html>
```